Self help book from Lantern Path needs awesome cover

We need a paperback and e-book cover for a self help book that is about to be published. The title is 'Quiet Harbor Awaits Wanderer: Channel Restless Hunger Toward Purpose'. Synopsis: Future You has achieved great success, and is trying to get an urgent communication to Present You to tell you how to master your mind and life so that you can achieve that greatness. If you don’t, the future won’t happen like it can, or should. Your destiny is to really make a difference in the lives of all of us. It’s not just for you. There are practical things you can do to think more clearly, and some mindfulness exercises to hone your skills. We currently do not have any color or graphic preferences, we're excited to see what you come up with! The final cover should express clarity, confidence, and a bit of urgency. Author's name is Marcus Pellow. Author name should be at the bottom.

```html
<!DOCTYPE html>
<html lang="en">
<head>
<meta charset="utf-8">
<title>Quiet Harbor Awaits Wanderer – Cover Spread</title>
<link href="https://fonts.googleapis.com/css2?family=Cinzel:wght@400;500&family=Tinos&display=swap" rel="stylesheet">
<style>
  :root {
    --page: #ffffff;
    --ink: #141414;
    --royal: #3b56a8;
    --sky-top: #d0ccdd;
    --sky-low: #efedf1;
    --horizon: #f4efec;
    --sea: #c6b9c7;
    --foam: #ddd0da;
    --sand: #cf8c44;
    --rule: #2a2a2a;
  }
  * { margin: 0; padding: 0; box-sizing: border-box; }
  html, body { width: 1200px; height: 1200px; overflow: hidden; background: var(--page); }
  .spread {
    position: absolute; left: 70px; top: 199px; width: 1060px; height: 803px; overflow: hidden;
  }
  .beach-photo {
    position: absolute; left: 0; top: 0; width: 1060px; height: 710px;
    background:
      linear-gradient(160deg, rgba(207,140,68,0) 62%, rgba(207,140,68,0.55) 100%),
      linear-gradient(180deg, var(--sky-top) 0%, var(--sky-low) 50%, var(--horizon) 62%, var(--sea) 72%, var(--foam) 86%, #b8a2a6 100%);
  }
  .author-band {
    position: absolute; left: 0; top: 710px; width: 1060px; height: 93px; background: var(--royal);
  }
  .author-band .author-name {
    position: absolute; left: 600px; top: 22px; width: 393px; text-align: center;
    font-family: "Cinzel", serif; font-weight: 500; font-size: 34px; line-height: 48px;
    letter-spacing: 9px; color: #fff; white-space: nowrap;
  }
  .title-block {
    position: absolute; text-align: center; font-family: "Cinzel", serif; color: var(--royal);
  }
  .title-block .ruled {
    display: flex; align-items: center; gap: 10px; color: var(--ink); line-height: 1;
  }
  .title-block .ruled::before, .title-block .ruled::after {
    content: ""; flex: 1; height: 1px; background: var(--rule);
  }
  .title-block .big { line-height: 1; white-space: nowrap; }
  .front-title { left: 588px; top: 60px; width: 420px; }
  .front-title .ruled.top { font-size: 38px; }
  .front-title .big.first { font-size: 104px; margin-top: 6px; }
  .front-title .ruled.mid { font-size: 36px; margin-top: 2px; }
  .front-title .big.second { font-size: 70px; margin-top: 4px; }
  .subtitle {
    position: absolute; left: 578px; top: 333px; width: 440px; text-align: center;
    font-family: "Tinos", serif; font-size: 32px; line-height: 38px; color: var(--ink);
  }
  .back-title { left: 132px; top: 49px; width: 262px; }
  .back-title .ruled.top { font-size: 22px; }
  .back-title .big.first { font-size: 64px; margin-top: 2px; }
  .back-title .ruled.mid { font-size: 22px; }
  .back-title .big.second { font-size: 42px; margin-top: 4px; }
  .synopsis {
    position: absolute; left: 73px; top: 219px; width: 383px;
    font-family: "Tinos", serif; font-size: 14px; line-height: 18.6px; letter-spacing: 0.6px;
    color: var(--ink); text-align: justify; text-align-last: center;
  }
  .synopsis p + p { margin-top: 18.6px; }
  .spine-title, .spine-author {
    position: absolute; left: 520px; height: 20px;
    transform-origin: 0 0; transform: translateX(20px) rotate(90deg);
    font-family: "Cinzel", serif; font-size: 16px; line-height: 20px; white-space: nowrap; color: var(--ink);
  }
  .spine-title { top: 56px; width: 370px; }
  .spine-author { top: 518px; width: 150px; }
  .spine-title .blue { color: var(--royal); }
</style>
</head>
<body>
<div class="spread">
  <div class="beach-photo" role="img" aria-label="Photograph of a calm beach at sunrise: pale cloudy sky, sea with foaming waves and golden sand"></div>

  <div class="title-block back-title">
    <div class="ruled top">QUIET</div>
    <div class="big first">HARBOR</div>
    <div class="ruled mid">AWAITS</div>
    <div class="big second">WANDERER</div>
  </div>

  <div class="synopsis">
    <p>Future You has achieved great success, and is trying to get an urgent communication to Present You to tell you how to master your mind and life so that you can achieve that greatness. If you don’t, the future won’t happen like it can, or should.</p>
    <p>Your destiny is to really make a difference in the lives of all of us. It’s not just for you. There are practical things you can do to think more clearly, and some mindfulness exercises to hone your skills. Begin today, and let your future self lead the way forward.</p>
  </div>

  <div class="spine-title">QUIET <span class="blue">HARBOR</span> AWAITS <span class="blue">WANDERER</span></div>
  <div class="spine-author">AUTHOR’S NAME</div>

  <div class="title-block front-title">
    <div class="ruled top">QUIET</div>
    <div class="big first">HARBOR</div>
    <div class="ruled mid">AWAITS</div>
    <div class="big second">WANDERER</div>
  </div>

  <div class="subtitle">Channel Restless Hunger<br>Toward Purpose</div>

  <div class="author-band">
    <div class="author-name">AUTHOR’S NAME</div>
  </div>
</div>
</body>
</html>
```